Flyer Frost Glow Cycle Tour
Zielgruppe
Wir sind DER Bikeshop in St. Moritz, welches auf 1800 m.ü.m. liegt. Wir verkaufen, vermieten uns servicen Bikes das ganze Jahr hindurch und haben auch 365 Tage im Jahr geöffnet. Wir sind die ersten, welche das Winterbiken für alle zugänglich gemacht haben und mit unseren Durafelt E-MTB ist das Fahren auf dem Schnee erstens sehr einfach und zweitens absolut sicher.
Aufgabenstellung
Flyerformat ist egal. Unsere Geschäftsfarben sind schwarz und gelb, der Hauptfont unseres Namens ist Marvelouz und wir arbeiten im High End Bereich. Gerne zwei Sprachen verwenden, evtl. Rückseite und Vorderseite gleich, nur die Sprachen ändern.
TEXT:
St. Moritz
Frost Glow Cycle Tour
Im Winter zu Biken ist ja schon verrückt, aber das ganze in der Nacht zu machen scheint ein Ding der Unmöglichkeit. Es ist das wahrscheinlich eines der coolsten Erlebnisse, welches es in St. Moritz im Winter gibt. Dank den Durafelt E-Bikes mit Spikes und unseren tollen Guides können Sie diese Ausfahrt auch sehr sicher erleben und sie ist für alle Personen, egal welchen Alters geeignet.
Auf speziellen Wunsch organisieren wir auch ein Outdoor-Abendessen, eine versteckte Alphütte zum Essen und Partymachen oder ganz einfach eine Champagnerpause im Pulverschnee dazu.
Dauer
1.5 – 2 Stunden
Inbegriffen
High End E-Bikes von Durafelt, Helm, Stirnlampe, heisses Getränk, Guide
Preis
ab Fr. 95.- pro Person (bei 8 Teilnehmern), Fr. 97.- bei 7 T., Fr. 100.- bei 6 T., Fr. 104.- bei 5 T., Fr. 110.- bei 4 T., Fr. 120.- bei 3 T., Fr. 140.- bei 2 T., Fr. 200.- bei einem Teilnemer.
Biking in winter is already crazy, but doing it at night seems impossible. It’s probably one of the coolest experiences you can have in St. Moritz in winter. Thanks to the Durafelt e-bikes with spikes and our great guides, you can also experience this ride very safely and it is suitable for all people, no matter what age.
On special request, we can also organise an outdoor dinner, a hidden alpine hut for eating and partying or simply a champagne break in the powder snow.
Duration
Included
High End E-Bikes von Durafelt, Helm, Stirnlampe, heisses Getränk, ..

```html
<!DOCTYPE html>
<html lang="de">
<head>
<meta charset="utf-8">
<title>Frost Glow Cycle Tour – Flyer DE / EN</title>
<link rel="stylesheet" href="https://fonts.googleapis.com/css2?family=Alfa+Slab+One&family=Rubik:wght@400;500;700&display=swap">
<style>
  :root {
    --ink: #0b0b0b;
    --yellow: #f7d417;
    --red: #d8262c;
    --white: #ffffff;
    --paper: #ffffff;
    --muted: #1a1a1a;
    --stage: #c4c4c4;
    --head-font: "Alfa Slab One", Georgia, serif;
    --body-font: "Rubik", Arial, sans-serif;
  }
  * { margin: 0; padding: 0; box-sizing: border-box; }
  html, body { width: 889px; height: 1200px; overflow: hidden; background: var(--stage); }
  .flyer-frame { position: absolute; top: 303px; width: 420px; height: 594px; box-shadow: 0 4px 14px rgba(0,0,0,0.25); }
  .frame-de { left: 16px; }
  .frame-en { left: 453px; }
  .flyer { position: absolute; left: 0; top: 0; width: 640px; height: 905px; transform: scale(0.65625); transform-origin: 0 0; background: var(--ink); overflow: hidden; font-family: var(--body-font); color: var(--white); }
  .flyer-shapes { position: absolute; inset: 0; }
  .place-name { font-family: var(--head-font); font-size: 31px; letter-spacing: 11px; fill: var(--ink); }
  .title { position: absolute; left: 0; right: 0; text-align: center; font-family: var(--head-font); font-weight: 400; line-height: 1; font-size: 52px; letter-spacing: 2px; }
  .title-top { top: 266px; color: var(--white); }
  .title-bottom { top: 321px; color: var(--yellow); }
  .date-box { position: absolute; top: 380px; left: 50%; transform: translateX(-50%); border: 3px solid var(--yellow); padding: 4px 14px 3px; font-family: var(--head-font); font-size: 23px; letter-spacing: 1px; white-space: nowrap; }
  .intro { position: absolute; top: 432px; left: 40px; right: 40px; text-align: center; font-size: 10.6px; line-height: 1.2; }
  .intro p + p { margin-top: 12px; }
  .fact { position: absolute; top: 535px; height: 56px; background: var(--red); text-align: center; display: flex; flex-direction: column; justify-content: center; }
  .fact-duration { left: 54px; width: 257px; }
  .fact-included { left: 326px; width: 257px; }
  .fact-label { font-family: var(--head-font); color: var(--yellow); font-size: 12px; letter-spacing: 1px; line-height: 1.1; }
  .fact-value-big { font-family: var(--head-font); font-size: 21px; letter-spacing: 1px; line-height: 1.1; }
  .fact-value { font-size: 10.6px; line-height: 1.2; }
  .price { position: absolute; top: 603px; left: 40px; right: 40px; text-align: center; font-size: 11px; line-height: 1.3; }
  .price-label { font-family: var(--head-font); color: var(--yellow); font-size: 14px; margin-right: 3px; }
  .sep { color: var(--yellow); font-weight: 700; }
  .contact { position: absolute; display: flex; align-items: center; gap: 5px; color: var(--muted); font-size: 11.5px; }
  .contact svg { width: 11px; height: 11px; flex: none; }
  .contact-address { top: 836px; left: 46px; }
  .contact-mail { top: 859px; left: 46px; }
  .contact-phone { top: 836px; left: 268px; }
  .contact-social { top: 859px; left: 268px; }
  .brand { position: absolute; top: 847px; left: 432px; width: 150px; text-align: center; font-weight: 700; font-size: 15px; letter-spacing: 5px; color: var(--ink); }
</style>
</head>
<body>
<svg width="0" height="0" style="position:absolute" aria-hidden="true">
  <defs>
    <linearGradient id="sky-scene" x1="0" y1="0" x2="0" y2="1">
      <stop offset="0" stop-color="#7a66c8"/>
      <stop offset="0.22" stop-color="#e07c8e"/>
      <stop offset="0.4" stop-color="#2a2438"/>
      <stop offset="0.62" stop-color="#3b4aa8"/>
      <stop offset="1" stop-color="#6b70d6"/>
    </linearGradient>
    <linearGradient id="town-scene" x1="0" y1="0" x2="0" y2="1">
      <stop offset="0" stop-color="#0b0b0b"/>
      <stop offset="0.5" stop-color="#232323"/>
      <stop offset="1" stop-color="#1a1a1a"/>
    </linearGradient>
    <radialGradient id="ride-forest" cx="0.5" cy="0.45" r="0.6">
      <stop offset="0" stop-color="#c9b58e"/><stop offset="1" stop-color="#1d2433"/>
    </radialGradient>
    <radialGradient id="ride-church" cx="0.5" cy="0.6" r="0.6">
      <stop offset="0" stop-color="#bfc0c4"/><stop offset="1" stop-color="#140e0a"/>
    </radialGradient>
    <radialGradient id="ride-snow" cx="0.5" cy="0.55" r="0.6">
      <stop offset="0" stop-color="#9ccf3a"/><stop offset="1" stop-color="#1c2230"/>
    </radialGradient>
  </defs>
</svg>

<!-- German flyer -->
<div class="flyer-frame frame-de">
<main class="flyer" lang="de">
  <svg class="flyer-shapes" width="640" height="905" viewBox="0 0 640 905">
    <defs><path id="place-arc-de" d="M30,210 Q320,252 610,210"/></defs>
    <g role="img" aria-label="Photo: sunset over snowy mountains and a frozen lake with a lone cyclist on the snow">
      <rect x="0" y="0" width="640" height="215" fill="url(#sky-scene)"/>
    </g>
    <path d="M0,160 Q320,218 640,160 L640,230 Q320,285 0,230 Z" fill="var(--yellow)"/>
    <path d="M0,230 Q320,285 640,230 L640,905 L0,905 Z" fill="var(--ink)"/>
    <text class="place-name" text-anchor="middle"><textPath href="#place-arc-de" startOffset="50%">•ST. MORITZ•</textPath></text>
    <g role="img" aria-label="Photo: dark night view over the village rooftops">
      <rect x="0" y="655" width="640" height="160" fill="url(#town-scene)" opacity="0.9"/>
    </g>
    <path d="M0,770 Q320,815 640,770 L640,905 L0,905 Z" fill="var(--yellow)"/>
    <path d="M0,795 Q320,840 640,795 L640,905 L0,905 Z" fill="var(--paper)"/>
    <g class="ride-photos">
      <circle cx="181" cy="740" r="72" fill="var(--ink)"/>
      <circle cx="321" cy="740" r="72" fill="var(--ink)"/>
      <circle cx="462" cy="740" r="72" fill="var(--ink)"/>
      <circle cx="181" cy="740" r="61" fill="url(#ride-forest)" stroke="var(--yellow)" stroke-width="3" role="img" aria-label="Photo: riders with headlamps lighting snowy trees"/>
      <circle cx="321" cy="740" r="61" fill="url(#ride-church)" stroke="var(--yellow)" stroke-width="3" role="img" aria-label="Photo: rider with helmet lamp in front of an illuminated tower"/>
      <circle cx="462" cy="740" r="61" fill="url(#ride-snow)" stroke="var(--yellow)" stroke-width="3" role="img" aria-label="Photo: rider in a green jacket on a snowy forest trail"/>
    </g>
  </svg>

  <h1 class="title title-top">FROST GLOW</h1>
  <h2 class="title title-bottom">CYCLE TOUR</h2>
  <div class="date-box">1.12.2024 - 28.2.2025</div>

  <div class="intro">
    <p>Im Winter zu Biken ist ja schon verrückt, aber das ganze in der Nacht zu machen scheint ein Ding der Unmöglichkeit. Es ist das wahrscheinlich eines der coolsten Erlebnisse, welches es in St. Moritz im Winter gibt. Dank den Durafelt E-Bikes mit Spikes und unseren tollen Guides können Sie diese Ausfahrt auch sehr sicher erleben und sie ist für alle Personen, egal welchen Alters geeignet.</p>
    <p>Auf speziellen Wunsch organisieren wir auch ein Outdoor-Abendessen, eine versteckte Alphütte zum Essen und Partymachen oder ganz einfach eine Champagnerpause im Pulverschnee dazu.</p>
  </div>

  <div class="fact fact-duration">
    <div class="fact-label">DAUER</div>
    <div class="fact-value-big">1.5 - 2 STUNDEN</div>
  </div>
  <div class="fact fact-included">
    <div class="fact-label">INBEGRIFFEN</div>
    <div class="fact-value">High End E-Bikes von Durafelt, Helm,<br>Stirnlampe, heisses Getränk, Guide</div>
  </div>

  <p class="price"><span class="price-label">PREIS</span> ab Fr. 95.- pro Person (bei 8 Teilnehmern) <span class="sep">•</span> Fr. 97.- bei 7 T <span class="sep">•</span> Fr. 100.- bei 6 T<br>Fr. 104.- bei 5 T <span class="sep">•</span> Fr. 110.- bei 4 T <span class="sep">•</span> Fr. 120.- bei 3 T <span class="sep">•</span> Fr. 140.- bei 2 T<br>Fr. 200.- bei einem Teilnemer.</p>

  <div class="contact contact-address">
    <svg viewBox="0 0 14 14"><path d="M7 0.8a4.6 4.6 0 0 0-4.6 4.6C2.4 9 7 13.4 7 13.4s4.6-4.4 4.6-8A4.6 4.6 0 0 0 7 0.8z" fill="var(--red)"/><circle cx="7" cy="5.3" r="1.8" fill="#fff"/></svg>
    Via Sela 14 | 7500 St. Moritz
  </div>
  <div class="contact contact-mail">
    <svg viewBox="0 0 14 14"><circle cx="7" cy="7" r="7" fill="var(--red)"/><rect x="3.5" y="4.5" width="7" height="5" fill="none" stroke="#fff" stroke-width="1"/><path d="M3.5 4.8 7 7.6l3.5-2.8" fill="none" stroke="#fff" stroke-width="1"/></svg>
    stmoritz@peakroll.ch
  </div>
  <div class="contact contact-phone">
    <svg viewBox="0 0 14 14"><circle cx="7" cy="7" r="7" fill="var(--red)"/><path d="M4.6 3.6l1.4-.3.8 1.9-.9.7a5 5 0 0 0 2.2 2.2l.7-.9 1.9.8-.3 1.4c-3.4.3-6.1-2.4-5.8-5.8z" fill="#fff"/></svg>
    +41 81 555 01 23
  </div>
  <div class="contact contact-social">
    <svg viewBox="0 0 14 14"><circle cx="7" cy="7" r="7" fill="var(--red)"/></svg>
    peakroll_stmoritz
  </div>
  <div class="brand">PEAKROLL</div>
</main>
</div>

<!-- English flyer -->
<div class="flyer-frame frame-en">
<main class="flyer" lang="en">
  <svg class="flyer-shapes" width="640" height="905" viewBox="0 0 640 905">
    <defs><path id="place-arc-en" d="M30,210 Q320,252 610,210"/></defs>
    <g role="img" aria-label="Photo: sunset over snowy mountains and a frozen lake with a lone cyclist on the snow">
      <rect x="0" y="0" width="640" height="215" fill="url(#sky-scene)"/>
    </g>
    <path d="M0,160 Q320,218 640,160 L640,230 Q320,285 0,230 Z" fill="var(--yellow)"/>
    <path d="M0,230 Q320,285 640,230 L640,905 L0,905 Z" fill="var(--ink)"/>
    <text class="place-name" text-anchor="middle"><textPath href="#place-arc-en" startOffset="50%">•ST. MORITZ•</textPath></text>
    <g role="img" aria-label="Photo: dark night view over the village rooftops">
      <rect x="0" y="655" width="640" height="160" fill="url(#town-scene)" opacity="0.9"/>
    </g>
    <path d="M0,770 Q320,815 640,770 L640,905 L0,905 Z" fill="var(--yellow)"/>
    <path d="M0,795 Q320,840 640,795 L640,905 L0,905 Z" fill="var(--paper)"/>
    <g class="ride-photos">
      <circle cx="181" cy="740" r="72" fill="var(--ink)"/>
      <circle cx="321" cy="740" r="72" fill="var(--ink)"/>
      <circle cx="462" cy="740" r="72" fill="var(--ink)"/>
      <circle cx="181" cy="740" r="61" fill="url(#ride-forest)" stroke="var(--yellow)" stroke-width="3" role="img" aria-label="Photo: riders with headlamps lighting snowy trees"/>
      <circle cx="321" cy="740" r="61" fill="url(#ride-church)" stroke="var(--yellow)" stroke-width="3" role="img" aria-label="Photo: rider with helmet lamp in front of an illuminated tower"/>
      <circle cx="462" cy="740" r="61" fill="url(#ride-snow)" stroke="var(--yellow)" stroke-width="3" role="img" aria-label="Photo: rider in a green jacket on a snowy forest trail"/>
    </g>
  </svg>

  <h1 class="title title-top">FROST GLOW</h1>
  <h2 class="title title-bottom">CYCLE TOUR</h2>
  <div class="date-box">1.12.2024 - 28.2.2025</div>

  <div class="intro">
    <p>Biking in winter is already crazy, but doing it at night seems impossible. It’s probably one of the coolest experiences you can have in St. Moritz in winter. Thanks to the Durafelt e-bikes with spikes and our great guides, you can also experience this ride very safely and it is suitable for all people, no matter what age.</p>
    <p>On special request, we can also organise an outdoor dinner, a hidden alpine hut for eating and partying or simply a champagne break in the powder snow.</p>
  </div>

  <div class="fact fact-duration">
    <div class="fact-label">DURATION</div>
    <div class="fact-value-big">1.5 - 2 STUNDEN</div>
  </div>
  <div class="fact fact-included">
    <div class="fact-label">INCLUDED</div>
    <div class="fact-value">High End E-Bikes from Durafelt,<br>helmet, headlamp, hot drink, guide</div>
  </div>

  <p class="price"><span class="price-label">PRICE</span> from Fr. 95.- per person (with 8 participants) <span class="sep">•</span> Fr. 97.- with 7 p<br>Fr. 100.- with 6 p <span class="sep">•</span> Fr. 104.- with 5 p <span class="sep">•</span> Fr. 110.- with 4 p <span class="sep">•</span> Fr. 120.- with 3 p<br>Fr. 140.- with 2 p <span class="sep">•</span> Fr. 200.- with one participant.</p>

  <div class="contact contact-address">
    <svg viewBox="0 0 14 14"><path d="M7 0.8a4.6 4.6 0 0 0-4.6 4.6C2.4 9 7 13.4 7 13.4s4.6-4.4 4.6-8A4.6 4.6 0 0 0 7 0.8z" fill="var(--red)"/><circle cx="7" cy="5.3" r="1.8" fill="#fff"/></svg>
    Via Sela 14 | 7500 St. Moritz
  </div>
  <div class="contact contact-mail">
    <svg viewBox="0 0 14 14"><circle cx="7" cy="7" r="7" fill="var(--red)"/><rect x="3.5" y="4.5" width="7" height="5" fill="none" stroke="#fff" stroke-width="1"/><path d="M3.5 4.8 7 7.6l3.5-2.8" fill="none" stroke="#fff" stroke-width="1"/></svg>
    stmoritz@peakroll.ch
  </div>
  <div class="contact contact-phone">
    <svg viewBox="0 0 14 14"><circle cx="7" cy="7" r="7" fill="var(--red)"/><path d="M4.6 3.6l1.4-.3.8 1.9-.9.7a5 5 0 0 0 2.2 2.2l.7-.9 1.9.8-.3 1.4c-3.4.3-6.1-2.4-5.8-5.8z" fill="#fff"/></svg>
    +41 81 555 01 23
  </div>
  <div class="contact contact-social">
    <svg viewBox="0 0 14 14"><circle cx="7" cy="7" r="7" fill="var(--red)"/></svg>
    peakroll_stmoritz
  </div>
  <div class="brand">PEAKROLL</div>
</main>
</div>
</body>
</html>
```